Business Brochure / White Paper

This white paper is a marketing document to showcase ourselves to other businesses (private hospitals and other premium healthcare providers). The document should consist of bold and beautiful graphics. As an example of the sort of thing that we mean, we have attached the "velmora sky lineage records" white paper. It should consist of several A4 pages.
The content for the white paper is attached. Note that the content document is only a scaffold for the white paper and the exact layout does not need to be followed (especially text boxes which have just been placed roughly). You are free to use your artistic license to move content around in order to make the document as catchy as possible.
We have also included graphics that we have purchased licenses to and that we encourage to be used as you see fit. Note that in some places we have added a note after two asterisks (i.e. **) when we would like you to add specific images/graphics.
All of the relevant documents and graphics/images to be used to make the white paper can be found at the below link:
https://www.filquarry.net/sh/zhtwmekbb41paxl/BBDN5K3TB8FWLPNTq1tGmeOWRc?dl=0
Feel free to ask any questions.
Good Luck!
Hi,
Thank you for your submissions so far.
Please use our dropbox link for an updated and much more specific brief on what we require in terms of content, layout, and components:
Please note that we must make a decision within 3 days' time.
Please also note that we cannot select a designer unless designs for ALL PAGES of the white paper are submitted.
Thank you and good luck!

```html
<!DOCTYPE html>
<html lang="en">
<head>
<meta charset="utf-8">
<title>Helixara – Product Line</title>
<link href="https://fonts.googleapis.com/css2?family=Montserrat:wght@600;700;800&family=Source+Sans+3:wght@400;600;700&display=swap" rel="stylesheet">
<style>
  :root {
    --backdrop: #e6e8eb;
    --paper: #ffffff;
    --navy: #14284a;
    --blue: #1a6fb8;
    --sky: #4aa8dc;
    --green: #6dbb45;
    --ink: #2c2f36;
    --muted: #6b7280;
    --rule: #cfd6df;
  }
  * { box-sizing: border-box; margin: 0; padding: 0; }
  html, body { width: 889px; height: 1200px; overflow: hidden; background: var(--backdrop); }
  body { font-family: "Source Sans 3", Arial, sans-serif; color: var(--ink); }

  .page {
    position: absolute; left: 30px; top: 24px; width: 829px; height: 1152px;
    background: var(--paper); box-shadow: 0 2px 10px rgba(0,0,0,.12);
    overflow: hidden;
  }
  .hero {
    height: 250px;
    background: linear-gradient(110deg, #dfe9f2 0%, #b8cfe2 40%, #7fa6c6 70%, #4d7ea8 100%);
  }
  .content { padding: 26px 60px 0; }
  .page-title {
    font-family: "Montserrat", Arial, sans-serif; font-weight: 800;
    font-size: 34px; letter-spacing: .5px; color: var(--navy);
    padding-bottom: 12px; border-bottom: 2px solid var(--rule);
    margin-bottom: 18px;
  }
  .product { margin-bottom: 16px; }
  .product h2 {
    font-family: "Montserrat", Arial, sans-serif; font-weight: 700;
    font-size: 16px; color: var(--blue); margin-bottom: 6px;
  }
  .product p { font-size: 13.4px; line-height: 1.5; text-align: justify; }

  .footer {
    position: absolute; left: 0; right: 0; bottom: 0; height: 92px;
    border-top: 3px solid var(--green);
    display: flex; align-items: center; padding: 0 40px 0 50px;
  }
  .brand { display: flex; align-items: center; gap: 10px; }
  .brand-dot { width: 30px; height: 30px; border-radius: 50%; background: var(--sky); }
  .brand-name {
    font-family: "Montserrat", Arial, sans-serif; font-weight: 700;
    font-size: 30px; color: var(--navy);
  }
  .tagline {
    margin-left: 70px; font-family: "Montserrat", Arial, sans-serif;
    font-weight: 700; font-size: 13px; line-height: 1.35; color: var(--navy);
    text-transform: uppercase;
  }
  .page-number {
    margin-left: auto; width: 46px; height: 46px; background: var(--blue);
    color: #fff; font-family: "Montserrat", Arial, sans-serif; font-weight: 700;
    font-size: 22px; display: flex; align-items: center; justify-content: center;
  }
</style>
</head>
<body>
  <main class="page">
    <div class="hero" role="img" aria-label="Photo of a hand touching a glowing digital interface with a DIAGNOSE button and a DNA helix"></div>

    <section class="content">
      <h1 class="page-title">PRODUCT LINE</h1>

      <article class="product">
        <h2>Whole Genome Sequencing</h2>
        <p>The human genome was first decoded in 2003, taking over 13 years and $2.7 billion to complete. Thanks to exponential advances in technology, helixaraTM can now do the same at only a fraction of the time and cost. Whole Genome Sequencing (WGS) provides a complete analysis of your patients' DNA and future proofs them so that dynamic updates can be generated as scientific discovery continues at its rapid pace.</p>
      </article>

      <article class="product">
        <h2>Whole Exome Sequencing</h2>
        <p>The "exome" is the known gene coding region of an individual's entire genome. In other words, it is where the real action takes place. Whole exome sequencing will provide most of the important answers that patients and physicians are seeking. Whole exome sequencing can therefore be considered to be more efficient, but less thorough, than whole genome sequencing.</p>
      </article>

      <article class="product">
        <h2>Disease Risk Genotyping</h2>
        <p>Prevention is always better than cure. Scientific research is moving at rapid speed and numerous genes have already been associated with a range of diseases, including cancers, heart conditions and diabetes. There are over 7,000 known inherited diseases affecting millions of individuals worldwide. In many cases, early recognition and management will significantly improve these individuals' quality and length of life.</p>
      </article>

      <article class="product">
        <h2>Pharmacogenomic Genotyping</h2>
        <p>Scientific research has shown that the response rate for many prescribed drugs is as low as 50% and that genetic factors can account for up to 95% of drug response variability and susceptibility. In other words, many of the billions of drugs prescribed every year are inadequately dosed, leading to side effects or no effects at all. This is why physicians around the world are turning to "precision prescribing". Pharmacogenomic testing allows for the proactive identification of appropriate drugs and dosages for a range of commonly prescribed and over-the-counter medications. In fact, several studies have shown that over 75% of people taking a generic test for medication compatibility learned information that is relevant to them.</p>
      </article>

      <article class="product">
        <h2>Other Genotyping Products</h2>
        <p>An ever growing number of tests are available depending on the specific needs and desires of your business. Microbiome, dietary, and family planning tests are just some examples to name a few.</p>
      </article>
    </section>

    <footer class="footer">
      <div class="brand">
        <span class="brand-dot"></span>
        <span class="brand-name">helixara</span>
      </div>
      <p class="tagline">We're helping to build<br>the future of good health</p>
      <div class="page-number">4</div>
    </footer>
  </main>
</body>
</html>
```